Banner for Firefighter themed Coffee Company

I need a banner for my home page of my coffee company. It is aimed at Firefighters and first responders in Australia.
I have attached an image i would like incorporated into the banner. Happy for the background to be removed as needed. Maybe incorporate fire and of coffee beans image in background. Or am happy to look at other designs that may suit. Serious with humorous undertones.
Think in the style of Copper Kettle Roasting House.
The text reads:
Built for the brave.
Serious coffee for a serious profession.
If possible can I have a web and mobile friendly version.
Target Market(s)
Australian Firefighters and First Responders

```html
<!DOCTYPE html>
<html lang="en">
<head>
<meta charset="UTF-8">
<title>Built for the Brave</title>
<link rel="stylesheet" href="https://fonts.googleapis.com/css2?family=Bebas+Neue&display=swap">
<style>
  :root {
    --bg-black: #07080a;
    --outline-white: #ffffff;
    --brand-red: #d7191c;
    --flame-orange: #e8611a;
    --flame-deep: #7a1a08;
    --coat-red: #5e1b1c;
    --coat-dark: #2a0d0e;
  }
  html, body {
    margin: 0;
    padding: 0;
    width: 1200px;
    height: 438px;
    overflow: hidden;
    background: var(--bg-black);
  }
  .hero-banner {
    position: relative;
    width: 1200px;
    height: 438px;
    background: var(--bg-black);
    overflow: hidden;
  }
  .hero-banner svg {
    display: block;
  }
  .headline {
    font-family: "Bebas Neue", "Arial Narrow", sans-serif;
    font-size: 180px;
    fill: none;
    stroke: var(--outline-white);
    stroke-width: 2.4;
  }
  .tagline {
    font-family: "Bebas Neue", "Arial Narrow", sans-serif;
    fill: var(--brand-red);
  }
  .tagline-initial { font-size: 124px; }
  .tagline-line { font-size: 46px; }
</style>
</head>
<body>
<main class="hero-banner">
  <svg width="1200" height="438" viewBox="0 0 1200 438" xmlns="http://www.w3.org/2000/svg">
    <defs>
      <radialGradient id="fireGlow" cx="0.5" cy="0.55" r="0.55">
        <stop offset="0" stop-color="var(--flame-orange)" stop-opacity="0.9"/>
        <stop offset="0.55" stop-color="var(--flame-deep)" stop-opacity="0.6"/>
        <stop offset="1" stop-color="var(--bg-black)" stop-opacity="0"/>
      </radialGradient>
      <linearGradient id="coatTone" x1="0" y1="0" x2="0" y2="1">
        <stop offset="0" stop-color="var(--coat-dark)"/>
        <stop offset="0.45" stop-color="var(--coat-red)"/>
        <stop offset="1" stop-color="var(--coat-dark)"/>
      </linearGradient>
    </defs>

    <rect class="fire-and-beans" x="300" y="40" width="900" height="398" fill="url(#fireGlow)"
          role="img" aria-label="Flames and scattered roasted coffee beans behind the firefighter"/>

    <text class="headline" x="24" y="199" textLength="1151" lengthAdjust="spacingAndGlyphs">BUILT FOR THE BRAVE</text>

    <path class="firefighter-photo" d="M440 438 L440 260 Q460 190 560 175 L650 160 L650 40 Q655 0 720 0 L860 0 Q895 0 895 40 L895 160 L980 180 Q1060 200 1065 280 L1065 438 Z"
          fill="url(#coatTone)" role="img"
          aria-label="Firefighter in helmet and turnout coat holding a steel coffee mug"/>

    <text class="tagline tagline-initial" x="24" y="356">A</text>
    <text class="tagline tagline-line" x="75" y="303">SERIOUS COFFEE FOR</text>
    <text class="tagline tagline-line" x="75" y="356">SERIOUS PROFESSION</text>
  </svg>
</main>
</body>
</html>
```